Vodka Soda brand identity design and label design

New vodka soda (hard seltzer) brand needs a brand identity design and label designs.

The brand name is VELMO

We produce vodka soda packaged in cans. They come in three flavours
- Raspberry and Lime
- Pina Colada
- Black Cherry

We would like to have the designs look similar (same template) but have one difference depending on the fruit flavour.

The final delivered package should contain
- brand identity design guide with a logo, font and colour schemes
- 3 label designs on the same template (label size 8.125 x 5 inches)

Some example designs of similar products are attached to the project.

Target Market(s)

Gender neutral, younger population

Colors
000000

Requirements
Must have
• Bright background and bright eye catching colours.

```html
<!DOCTYPE html>
<html lang="en">
<head>
<meta charset="utf-8">
<title>VELMO Hard Seltzer – Black Cherry Label</title>
<link rel="stylesheet" href="https://fonts.googleapis.com/css2?family=Oswald:wght@300;400;500;600;700&family=Montserrat:wght@600;700&display=swap">
<style>
  :root{
    --deep-purple:#2c1263;
    --purple:#5526a0;
    --violet:#8a4fd0;
    --pink:#e3288c;
    --magenta:#b5176f;
    --hot-pink:#ee3d9e;
    --white:#ffffff;
    --ink:#3a1878;
    --page:#f4f4f6;
  }
  *{box-sizing:border-box;margin:0;padding:0}
  html,body{width:1200px;height:900px;overflow:hidden;background:var(--page)}
  body{font-family:'Oswald',sans-serif;color:var(--white)}
  .label{position:absolute;left:30px;top:100px;width:1140px;height:700px;display:flex}
  .panel{position:relative;width:380px;height:700px;overflow:hidden}
  .panel-art{position:absolute;inset:0;width:100%;height:100%}

  /* left panel */
  .side-logo{position:absolute;left:118px;top:200px;font-weight:500;font-size:52px;letter-spacing:2px;
    transform:rotate(-90deg);transform-origin:left top;color:var(--white);top:360px}
  .warning{position:absolute;left:18px;top:540px;width:320px;font-weight:300;font-size:12px;line-height:1.4}
  .warning strong{font-weight:600;display:block;font-size:13px}

  /* front panel */
  .front{text-align:center}
  .brand-logo{position:absolute;left:0;right:0;top:50px;font-weight:500;font-size:112px;letter-spacing:4px;line-height:1;color:var(--white)}
  .product-type{position:absolute;left:0;right:0;top:172px;font-weight:700;font-size:70px;line-height:1;color:var(--pink)}
  .flavour{position:absolute;left:0;right:0;top:440px;font-weight:700;font-size:48px;line-height:1;color:var(--white)}
  .stats{position:absolute;left:10px;right:10px;top:505px;display:flex;justify-content:space-between}
  .stat{flex:1;font-weight:300;font-size:28px;line-height:1.05}
  .stat b{display:block;font-weight:600;font-size:36px}
  .stat + .stat{border-left:2px solid var(--white)}
  .descriptor{position:absolute;left:0;right:0;top:612px;font-weight:300;font-size:30px;letter-spacing:6px}

  /* back panel */
  .nutrition{position:absolute;left:128px;top:28px;width:236px;background:var(--white);color:var(--ink);padding:4px 6px 8px}
  .nutrition h2{font-weight:600;font-size:34px;line-height:1;border-bottom:6px solid var(--ink);padding-bottom:2px}
  .nutrition .serving{font-size:14px;line-height:1.2;border-bottom:5px solid var(--ink);padding:2px 0 3px}
  .nutrition .amount{font-family:'Montserrat',sans-serif;font-weight:700;font-size:12px;padding-top:4px}
  .nutrition .calories{font-family:'Montserrat',sans-serif;font-weight:700;font-size:15px;border-bottom:5px solid var(--ink);line-height:1}
  .nutrition .calories span{font-size:30px}
  .nutrition .dv{text-align:right;font-size:13px;border-bottom:3px solid var(--ink);padding:2px 0}
  .nutrition .row{display:flex;justify-content:space-between;font-size:14px;border-bottom:2px solid var(--ink);padding:3px 4px 2px 0}
  .nutrition .row.indent{padding-left:8px}
  .nutrition .note{font-weight:300;font-size:12px;line-height:1.3;padding-top:5px}
  .ingredients{position:absolute;left:140px;top:472px;width:230px;font-size:15px;font-weight:300;line-height:1.45}
  .ingredients strong{font-weight:600}
  .recycle{position:absolute;left:22px;top:530px;width:40px;height:40px}
  .volume{position:absolute;left:16px;top:590px;font-weight:600;font-size:28px}
</style>
</head>
<body>
<main class="label">
  <section class="panel panel-warning">
    <svg class="panel-art" viewBox="0 0 380 700" preserveAspectRatio="none" role="img" aria-label="Space illustration: pink rocket launching over pink mountains on a purple starry sky">
      <defs>
        <linearGradient id="sky-a" x1="0" y1="0" x2="0" y2="1">
          <stop offset="0" stop-color="#2c1263"/><stop offset=".45" stop-color="#6a32b4"/>
          <stop offset=".62" stop-color="#7a2aa0"/><stop offset=".7" stop-color="#e3288c"/>
          <stop offset="1" stop-color="#b5176f"/>
        </linearGradient>
      </defs>
      <rect width="380" height="700" fill="url(#sky-a)"/>
    </svg>
    <div class="side-logo">VELMO</div>
    <p class="warning"><strong>GOVERNMENT WARNING:</strong>(1) According to the Surgeon General, women should not drink alcoholic beverages during pregnancy because of the risk of birth defects. (2) Consumption of alcoholic beverages impairs your ability to drive a car or operate machinery, and may cause health problems.</p>
  </section>

  <section class="panel front">
    <svg class="panel-art" viewBox="0 0 380 700" preserveAspectRatio="none" role="img" aria-label="Space illustration: ringed pink planet rising over pink mountains on a purple starry sky">
      <defs>
        <linearGradient id="sky-b" x1="0" y1="0" x2="0" y2="1">
          <stop offset="0" stop-color="#2c1263"/><stop offset=".35" stop-color="#6a32b4"/>
          <stop offset=".5" stop-color="#c0306e"/><stop offset=".62" stop-color="#e3288c"/>
          <stop offset="1" stop-color="#b5176f"/>
        </linearGradient>
      </defs>
      <rect width="380" height="700" fill="url(#sky-b)"/>
    </svg>
    <h1 class="brand-logo">VELMO</h1>
    <p class="product-type">HARD SELTZER</p>
    <p class="flavour">BLACK CHERRY</p>
    <div class="stats">
      <p class="stat"><b>100</b>calories</p>
      <p class="stat"><b>4.0%</b>alc/vol</p>
      <p class="stat"><b>0g</b>sugar</p>
    </div>
    <p class="descriptor">HARD SPARKLING WATER</p>
  </section>

  <section class="panel panel-info">
    <svg class="panel-art" viewBox="0 0 380 700" preserveAspectRatio="none" role="img" aria-label="Space illustration: planet ring, galaxy swirl and pink mountains on a purple starry sky">
      <defs>
        <linearGradient id="sky-c" x1="0" y1="0" x2="0" y2="1">
          <stop offset="0" stop-color="#2c1263"/><stop offset=".45" stop-color="#6a32b4"/>
          <stop offset=".6" stop-color="#7a2aa0"/><stop offset=".68" stop-color="#e3288c"/>
          <stop offset="1" stop-color="#b5176f"/>
        </linearGradient>
      </defs>
      <rect width="380" height="700" fill="url(#sky-c)"/>
    </svg>
    <div class="nutrition">
      <h2>Nutrition Facts</h2>
      <p class="serving">1 serving per container<br>Serving size 1 can (355mL/12fl.oz.)</p>
      <p class="amount">Amount per serving</p>
      <p class="calories">Calories <span>100</span></p>
      <p class="dv">% Daily Value</p>
      <p class="row"><span>Total Fat 0g</span><span>0%</span></p>
      <p class="row"><span>Sodium 20mg</span><span>1%</span></p>
      <p class="row"><span>Total Carbohydrate 2g</span><span>1%</span></p>
      <p class="row indent"><span>Total Sugars 2g</span><span></span></p>
      <p class="row indent"><span>Includes 2 Added Sugars</span><span>4%</span></p>
      <p class="row"><span>Protein 0g</span><span>0%</span></p>
      <p class="note">Not a significant source of total fat, saturated fat, trans fat, cholesterol, dietary fiber, protein, vitamin D, calcium, iron and potassium.</p>
    </div>
    <p class="ingredients"><strong>Ingredients:</strong><br>vodka, lime juice, raspberry.<br><strong>Made in: Canada</strong></p>
    <svg class="recycle" viewBox="0 0 40 40" aria-label="Recyclable">
      <g fill="none" stroke="#ffffff" stroke-width="4" stroke-linejoin="round">
        <path d="M14 8 L20 3 L26 12"/><path d="M31 18 L35 27 L24 32"/><path d="M12 32 L4 27 L9 17"/>
      </g>
    </svg>
    <p class="volume">355ml</p>
  </section>
</main>
</body>
</html>
```